Beauty Therapy Web Design

I need a web page design for a small beauty therapy clinic, the owner is currently the only beauty therapist working there.
We require the following pages:
Home
About
Treatments
Nails
Courses
Contact
I will attach the clinics business card, treatment menu and signage so that you get a feeling for the branding colours etc.
This is the first website for the beauty therapist, she would like to attract new clients and also tourists that come in on the cruise ships. The thing that sets her apart from other clinics is that she welcomes texting for appointments.
I have selected refundable because I have never done this before so I don't know what to expect, I have the full intention of going through with it as long as I get a good design.
Feel free to ask for further information
Reason: Project extended as I am away for work and am unable to meet with the owner.
Target Market(s)
Females 18 to 50
Industry/Entity Type
Business
Look and feel
Each slider illustrates characteristics of the customer's brand and the style your logo design should communicate.

```html
<!DOCTYPE html>
<html lang="en">
<head>
<meta charset="utf-8">
<title>Lumiere Beauty Therapy</title>
<link rel="stylesheet" href="https://fonts.googleapis.com/css2?family=Cormorant+Garamond:ital,wght@1,500;1,600&family=Open+Sans:wght@400;600&display=swap">
<style>
  :root {
    --purple: #6a559a;
    --purple-text: #5b4a94;
    --gold: #b9974a;
    --white: #ffffff;
    --rule: #7b6aa8;
  }
  * { box-sizing: border-box; margin: 0; padding: 0; }
  html, body { width: 960px; height: 1200px; overflow: hidden; }
  body {
    position: relative;
    background: var(--white);
    font-family: "Open Sans", sans-serif;
    color: var(--purple-text);
  }
  .header-band { position: absolute; left: 0; top: 0; width: 960px; height: 340px; background: var(--purple); }
  .booking-line {
    position: absolute; right: 92px; top: 14px;
    font-family: "Cormorant Garamond", serif; font-style: italic; font-weight: 500;
    font-size: 15px; color: var(--gold);
  }
  .brand { position: absolute; left: 108px; top: 30px; color: var(--gold); font-weight: 400; }
  .brand-name { display: block; font-size: 46px; line-height: 56px; letter-spacing: 1px; }
  .brand-sub { display: block; font-size: 19px; line-height: 24px; letter-spacing: 1px; }
  .main-nav { position: absolute; top: 120px; left: 454px; display: flex; }
  .main-nav a {
    color: var(--white); text-decoration: none; font-size: 15px; line-height: 26px;
    padding: 0 6px; margin-right: 6px; border-radius: 4px;
  }
  .main-nav a.active { background: var(--gold); }
  .main-nav a:nth-child(3) { margin-right: 12px; }
  .main-nav a:nth-child(4) { margin-right: 12px; }

  .hero { position: absolute; left: 96px; top: 162px; width: 769px; height: 318px; }
  .hero-panel {
    position: absolute; left: 0; top: 0; width: 291px; height: 318px;
    background: var(--purple); border: 1px solid var(--gold); border-right: none;
    border-radius: 6px 0 0 6px;
  }
  .hero-title {
    position: absolute; left: 29px; top: 46px;
    font-family: "Cormorant Garamond", serif; font-style: italic; font-weight: 500;
    font-size: 29px; color: var(--gold); border-bottom: 1px solid var(--gold); line-height: 32px;
  }
  .service-list { position: absolute; list-style: none; top: 134px; }
  .service-list li { color: var(--white); font-size: 18px; line-height: 24px; padding-left: 14px; position: relative; }
  .service-list li::before {
    content: ""; position: absolute; left: 0; top: 9px; width: 8px; height: 8px;
    border-radius: 50%; background: var(--white);
  }
  .service-list.col-a { left: 34px; }
  .service-list.col-b { left: 128px; }
  .btn {
    position: absolute; display: inline-block; text-decoration: none;
    font-size: 14px; font-weight: 600; border-radius: 6px; text-align: center;
  }
  .hero .btn { left: 78px; top: 262px; width: 134px; height: 27px; line-height: 27px; background: var(--white); color: var(--purple); }
  .hero-photo {
    position: absolute; left: 291px; top: 0; width: 478px; height: 318px;
    background: linear-gradient(160deg, #eef0f4 0%, #e6dcd6 45%, #d9b8a6 70%, #c9a497 100%);
  }

  .intro { position: absolute; left: 96px; top: 498px; width: 764px; }
  .section-heading {
    font-family: "Cormorant Garamond", serif; font-style: italic; font-weight: 500;
    color: var(--gold); font-size: 24px; line-height: 28px;
  }
  .intro p { margin-top: 8px; font-size: 12px; line-height: 16px; }
  .rule { position: absolute; left: 96px; width: 761px; height: 1px; background: var(--rule); }

  .card {
    position: absolute; top: 661px; width: 248px; height: 159px;
    background: var(--purple); border-radius: 6px; text-align: center; color: var(--white);
  }
  .card h2 { font-size: 20px; font-weight: 600; line-height: 24px; margin-top: 9px; }
  .card-photo { width: 139px; height: 92px; margin: 4px auto 0; border: 1px solid var(--gold); }
  .card p {
    font-family: "Cormorant Garamond", serif; font-style: italic; font-weight: 500;
    font-size: 16px; line-height: 20px; margin-top: 2px;
  }
  .card-nails { left: 94px; }
  .card-nails .card-photo { background: linear-gradient(135deg, #f4f6f4, #e4c6b4 60%, #c7d9b5); }
  .card-treat { left: 354px; }
  .card-treat .card-photo { background: linear-gradient(135deg, #f1eeee, #e5c7b8 55%, #d8d6d8); }
  .card-courses { left: 614px; }
  .card-courses .card-photo { background: linear-gradient(135deg, #c9a47d, #7a4a2c 55%, #3c2418); }

  .location { position: absolute; left: 96px; top: 876px; width: 260px; }
  .info-lines p { font-size: 13px; line-height: 24px; }
  .location .info-lines { margin-top: 6px; padding-left: 2px; }
  .map { position: absolute; left: 1px; top: 87px; width: 254px; height: 159px; background: linear-gradient(135deg, #ebe8e2, #e1ddd4); }
  .map-links { position: absolute; left: 42px; top: 252px; font-size: 9.5px; color: var(--gold); white-space: nowrap; }
  .map-links a { color: var(--gold); }
  .map-links span { margin: 0 12px; }
  .divider { position: absolute; left: 479px; top: 886px; width: 1px; height: 236px; background: var(--purple-text); }
  .vouchers { position: absolute; left: 503px; top: 876px; }
  .vouchers .info-lines { margin-top: 6px; }
  .holiday { position: absolute; left: 500px; top: 1012px; }
  .holiday .info-lines { margin-top: 8px; }
  .side-btn { left: 728px; top: 1098px; width: 124px; height: 25px; line-height: 25px; background: var(--purple); color: var(--white); font-weight: 400; font-size: 13px; }

  .footer { position: absolute; left: 0; top: 1153px; width: 960px; height: 47px; background: var(--purple); color: var(--white); }
  .footer-nav { position: absolute; left: 94px; top: 16px; display: flex; gap: 13px; font-size: 11px; }
  .footer-nav a { color: var(--white); text-decoration: none; }
  .footer-nav a.active { color: var(--gold); text-decoration: underline; }
  .copyright { position: absolute; right: 104px; top: 18px; font-size: 11px; }
</style>
</head>
<body>
  <div class="header-band"></div>
  <p class="booking-line">Book Your Treaments, Call or Text: 07 555 0182 / 021 555 0746</p>
  <div class="brand">
    <span class="brand-name">Lumiere</span>
    <span class="brand-sub">BEAUTY THERAPY</span>
  </div>
  <nav class="main-nav">
    <a class="active" href="#">Home</a>
    <a href="#">About</a>
    <a href="#">Nails</a>
    <a href="#">Treatments</a>
    <a href="#">Courses</a>
    <a href="#">Contact</a>
  </nav>

  <section class="hero">
    <div class="hero-panel">
      <h1 class="hero-title">Affordable Treatments</h1>
      <ul class="service-list col-a"><li>Nail</li><li>Waxing</li><li>Pedicure</li><li>Facials</li></ul>
      <ul class="service-list col-b"><li>Massage</li><li>Manicure</li><li>Spray On Tan</li><li>Men’s Waxing</li></ul>
      <a class="btn" href="#">More Information</a>
    </div>
    <div class="hero-photo" role="img" aria-label="Photo of a client relaxing during a hot stone massage"></div>
  </section>

  <section class="intro">
    <h2 class="section-heading">Lumiere Beauty Therapy</h2>
    <p>Lorem Ipsum is simply dummy text of the printing and typesetting industry. Lorem Ipsum has been the industry's standard dummy text ever since the 1500s, when an unknown printer took a galley of type and scrambled it to make a type specimen book. It has survived not only five centuries, but also the leap into electronic typesetting, remaining essentially unchanged. It was popularised in the 1960s with the release of Typeset sheets containing Lorem Ipsum passages, and more recently with desktop publishing soft-ware like Quill PageSetter including versions of Lorem Ipsum.</p>
  </section>
  <div class="rule" style="top:630px"></div>

  <a class="card card-nails">
    <h2>Nail Treatments</h2>
    <div class="card-photo" role="img" aria-label="Photo of a pedicure with painted toenails"></div>
    <p>View our full range of nail treatments</p>
  </a>
  <a class="card card-treat">
    <h2>Treatments</h2>
    <div class="card-photo" role="img" aria-label="Photo of hands receiving a moisturising treatment"></div>
    <p>View our full range of treatments</p>
  </a>
  <a class="card card-courses">
    <h2>Courses</h2>
    <div class="card-photo" role="img" aria-label="Photo of a facial mask treatment"></div>
    <p>View our full range of courses</p>
  </a>
  <div class="rule" style="top:858px"></div>

  <section class="location">
    <h2 class="section-heading">Our Location</h2>
    <div class="info-lines">
      <p>Cnr Kowhai St &amp; Harbour Rd,</p>
      <p>Bayview Heights</p>
    </div>
    <div class="map" role="img" aria-label="Street map showing the clinic location"></div>
    <p class="map-links"><a href="#">Get Directions</a><span>|</span><a href="#">View Larger Map</a></p>
  </section>
  <div class="divider"></div>

  <section class="vouchers">
    <h2 class="section-heading">Gift Vouchers</h2>
    <div class="info-lines">
      <p>Treat your loved one on that special occasion with our</p>
      <p>Gift Vouchers</p>
      <p>Vouchers for all buddets starting from $10</p>
    </div>
  </section>
  <section class="holiday">
    <h2 class="section-heading">Here on Holiday?</h2>
    <div class="info-lines">
      <p>Why not try one of our affordable courses to help you unwind.</p>
    </div>
  </section>
  <a class="btn side-btn" href="#">More Information</a>

  <footer class="footer">
    <nav class="footer-nav">
      <a class="active" href="#">Home</a>
      <a href="#">About</a>
      <a href="#">Nails</a>
      <a href="#">Treatments</a>
      <a href="#">Courses</a>
      <a href="#">Contact</a>
      <a href="#">Site Map</a>
    </nav>
    <p class="copyright">© Copyright Lumiere Beauty Therapy 2012</p>
  </footer>
</body>
</html>
```